Hobby beekeepers need a honey jar label

My wife and I are hobby beekeepers. We have 5 bee colonies, which are located on the property in an idyllic lake location.

The honey is said to have the name "meadowglen honey". A photo with the location of the bee colonies is attached and is to be integrated into the design as a supporting element.

The term "beekeeping in the pines" should be integrated together with the logo. The logo (stylized house with wave) is already used by us and should be adopted unchanged (shape, color can be changed), please replace "Praxis im Hain" with "Imkerei Tannengrund".

We also need our address on the label: "Konstantin and Jutta Brüggl, Birkenwinkl 7, 84172 Lindach am Forst".

We need labels for honey jars (format 1 large - width x height 120 mm x 57 mm // format 2 small - width x height 70 mm x 35 mm).

Target Market(s)

Customers who are willing to pay a high but justified price for a top honey in a loving, small-scale craft from the best location (meadowglen).

Requirements
Must have
• 1) A recognizable connection between the image (location of the bee colonies) and the name of the honey: "meadowglen honey".
2) Compliance with the "large" and "small" dimensions that are important for printing the labels.
3) Integration of the logo (house with wave) with the lettering "Imkerei Tannengrund"
4) Address line: "Imkerei Tannengrund - Konstantin & Jutta Brüggl, Birkenwinkl 7, 84172 Rott"
Nice to have
• I am happy when the label reflects the appreciation of nature and the loving care for the bees.
Should not have
• Classic organic touch

```html
<!DOCTYPE html>
<html lang="de">
<head>
<meta charset="utf-8">
<title>Meadowglen-Honing – Etikettenentwürfe</title>
<link href="https://fonts.googleapis.com/css2?family=Bebas+Neue&family=Barlow+Semi+Condensed:wght@500;600&family=Barlow:wght@400;500;600&family=Great+Vibes&display=swap" rel="stylesheet">
<style>
  :root {
    --stage: #e4e8e8;
    --variant-mark: #3d4a52;
    --panel-dark: #2b2d31;
    --cream: #f8f2e6;
    --ink: #262a30;
    --leaf-line: #a8d43a;
    --leaf-light: #8ef04a;
    --leaf-deep: #3fae12;
    --honey: #e9b21c;
    --honey-wash: #efd78a;
  }
  html, body {
    margin: 0;
    padding: 0;
    width: 1200px;
    height: 1000px;
    overflow: hidden;
    background: var(--stage);
  }
  .canvas {
    position: relative;
    width: 1200px;
    height: 1000px;
  }
  .variant-mark {
    position: absolute;
    left: 68px;
    font-family: "Bebas Neue", "Oswald", sans-serif;
    font-size: 200px;
    line-height: 1;
    color: var(--variant-mark);
  }
  .variant-mark--a { top: 185px; }
  .variant-mark--b { top: 662px; }
  .label {
    position: absolute;
    left: 192px;
    width: 816px;
    height: 386px;
    box-shadow: 0 10px 22px rgba(0, 0, 0, 0.18);
  }
  .label--a { top: 69px; }
  .label--b { top: 546px; }
  .label svg { display: block; }
  .panel { fill: var(--panel-dark); }
  .center-field { fill: var(--cream); }
  .hex-frame { fill: none; stroke: var(--leaf-line); stroke-width: 1.3; }
  .arc-title {
    font-family: "Barlow", sans-serif;
    font-weight: 500;
    font-size: 17px;
    letter-spacing: 3px;
    fill: var(--ink);
  }
  .house-name {
    font-family: "Barlow", sans-serif;
    font-weight: 600;
    font-size: 13px;
    fill: var(--ink);
  }
  .house-dot { fill: var(--ink); }
  .honey-title {
    font-family: "Barlow Semi Condensed", sans-serif;
    font-weight: 600;
    font-size: 34px;
    fill: var(--ink);
  }
  .honey-drip { fill: var(--honey); }
  .sketch-hex { fill: none; stroke: var(--ink); stroke-width: 1.2; }
  .bee-spot { fill: #d9d3c6; }
  .comb-spot { fill: #e8e2d4; }
  .rule { stroke: var(--ink); stroke-width: 1.5; }
  .rule--short { stroke-width: 1.2; }
  .address {
    font-family: "Barlow", sans-serif;
    font-weight: 400;
    font-size: 17px;
    fill: var(--ink);
  }
  .brush-band { fill: var(--honey-wash); }
  .script-title {
    font-family: "Great Vibes", cursive;
    font-size: 46px;
    fill: var(--ink);
  }
  .sub-title {
    font-family: "Barlow Semi Condensed", sans-serif;
    font-weight: 600;
    font-size: 19px;
    fill: var(--ink);
  }
</style>
</head>
<body>
<main class="canvas">

  <div class="variant-mark variant-mark--a">A</div>
  <div class="variant-mark variant-mark--b">B</div>

  <!-- Variant A -->
  <section class="label label--a" aria-label="Etikett Variante A">
    <svg width="816" height="386" viewBox="0 0 816 386">
      <defs>
        <linearGradient id="leafA" x1="0" y1="0" x2="0" y2="1">
          <stop offset="0" stop-color="var(--leaf-light)"/>
          <stop offset="1" stop-color="var(--leaf-deep)"/>
        </linearGradient>
        <path id="arcA" d="M 288 90 A 160 160 0 0 1 528 90"/>
      </defs>

      <rect class="panel" x="0" y="0" width="211" height="386"/>
      <rect class="center-field" x="211" y="0" width="394" height="386"/>
      <rect class="panel" x="605" y="0" width="211" height="386"/>

      <!-- left photo column -->
      <polygon class="hex-frame" points="198,95 169,145 111,145 82,95 111,45 169,45"/>
      <polygon class="hex-frame" points="196,205 167,255 109,255 80,205 109,155 167,155"/>
      <polygon class="hex-frame" points="200,310 160,379 80,379 40,310 80,241 160,241"/>
      <g role="img" aria-label="Foto: Bienenstand am Teich im Grünen">
        <polygon fill="url(#leafA)" points="170,52 145,97 93,97 68,52 93,7 145,7"/>
        <polygon fill="url(#leafA)" points="126,163 98,214 40,214 12,163 40,112 98,112"/>
        <polygon fill="url(#leafA)" points="188,287 153,351 83,351 48,287 83,223 153,223"/>
      </g>

      <!-- right photo column -->
      <polygon class="hex-frame" points="765,75 735,127 675,127 645,75 675,23 735,23"/>
      <polygon class="hex-frame" points="755,170 727,218 673,218 645,170 673,122 727,122"/>
      <polygon class="hex-frame" points="788,295 751,360 676,360 638,295 676,230 751,230"/>
      <g role="img" aria-label="Foto: Bienenstand am Teich im Grünen">
        <polygon fill="url(#leafA)" points="798,72 773,117 723,117 698,72 723,27 773,27"/>
        <polygon fill="url(#leafA)" points="720,140 696,183 647,183 623,140 647,97 696,97"/>
        <polygon fill="url(#leafA)" points="776,267 740,333 662,333 626,267 662,201 740,201"/>
      </g>

      <!-- centre -->
      <text class="arc-title"><textPath href="#arcA" startOffset="50%" text-anchor="middle">IMKEREI TANNENGRUND</textPath></text>
      <rect class="house-dot" x="402" y="68" width="12" height="12"/>
      <text class="house-name" x="408" y="99" text-anchor="middle">Imkerei</text>
      <text class="house-name" x="408" y="113" text-anchor="middle">Tannengrund</text>

      <rect class="honey-drip" x="459" y="0" width="12" height="152"/>
      <circle class="honey-drip" cx="465" cy="154" r="14"/>
      <text class="honey-title" x="451" y="166" text-anchor="end" textLength="206" lengthAdjust="spacingAndGlyphs">MEADOWGLEN-H</text>
      <text class="honey-title" x="480" y="166" textLength="88" lengthAdjust="spacingAndGlyphs">NING</text>

      <polygon class="sketch-hex" points="466,245 428,310 353,310 316,245 353,180 428,180"/>
      <polygon class="sketch-hex" points="496,245 459,310 384,310 346,245 384,180 459,180"/>
      <polygon class="sketch-hex" points="458,240 433,283 383,283 358,240 383,197 433,197"/>
      <ellipse class="bee-spot" cx="408" cy="236" rx="36" ry="26" role="img" aria-label="Zeichnung einer Honigbiene"/>

      <line class="rule" x1="251" y1="314" x2="565" y2="314"/>
      <text class="address" x="408" y="344" text-anchor="middle" textLength="296" lengthAdjust="spacingAndGlyphs">KONSTANTIN AND JUTTA BRÜGGL</text>
      <text class="address" x="408" y="365" text-anchor="middle" textLength="314" lengthAdjust="spacingAndGlyphs">BIRKENWINKL 7, 84172 LINDACH AM FORST</text>
    </svg>
  </section>

  <!-- Variant B -->
  <section class="label label--b" aria-label="Etikett Variante B">
    <svg width="816" height="386" viewBox="0 0 816 386">
      <defs>
        <linearGradient id="leafB" x1="0" y1="0" x2="0" y2="1">
          <stop offset="0" stop-color="var(--leaf-light)"/>
          <stop offset="1" stop-color="var(--leaf-deep)"/>
        </linearGradient>
        <path id="arcB" d="M 288 88 A 160 160 0 0 1 528 88"/>
      </defs>

      <rect class="panel" x="0" y="0" width="211" height="386"/>
      <rect class="center-field" x="211" y="0" width="394" height="386"/>
      <rect class="panel" x="605" y="0" width="211" height="386"/>

      <polygon class="hex-frame" points="198,95 169,145 111,145 82,95 111,45 169,45"/>
      <polygon class="hex-frame" points="196,205 167,255 109,255 80,205 109,155 167,155"/>
      <polygon class="hex-frame" points="200,310 160,379 80,379 40,310 80,241 160,241"/>
      <g role="img" aria-label="Foto: Bienenstand am Teich im Grünen">
        <polygon fill="url(#leafB)" points="170,52 145,97 93,97 68,52 93,7 145,7"/>
        <polygon fill="url(#leafB)" points="126,163 98,214 40,214 12,163 40,112 98,112"/>
        <polygon fill="url(#leafB)" points="188,287 153,351 83,351 48,287 83,223 153,223"/>
      </g>

      <polygon class="hex-frame" points="765,75 735,127 675,127 645,75 675,23 735,23"/>
      <polygon class="hex-frame" points="755,170 727,218 673,218 645,170 673,122 727,122"/>
      <polygon class="hex-frame" points="788,295 751,360 676,360 638,295 676,230 751,230"/>
      <g role="img" aria-label="Foto: Bienenstand am Teich im Grünen">
        <polygon fill="url(#leafB)" points="798,72 773,117 723,117 698,72 723,27 773,27"/>
        <polygon fill="url(#leafB)" points="720,140 696,183 647,183 623,140 647,97 696,97"/>
        <polygon fill="url(#leafB)" points="776,267 740,333 662,333 626,267 662,201 740,201"/>
      </g>

      <text class="arc-title"><textPath href="#arcB" startOffset="50%" text-anchor="middle">IMKEREI TANNENGRUND</textPath></text>
      <rect class="house-dot" x="402" y="66" width="12" height="12"/>
      <text class="house-name" x="408" y="97" text-anchor="middle">Imkerei</text>
      <text class="house-name" x="408" y="111" text-anchor="middle">Tannengrund</text>

      <path class="brush-band" d="M 248 140 Q 400 124 572 150 L 573 174 Q 420 170 240 190 Z" role="img" aria-label="Pinselstrich in Honiggelb"/>
      <text class="script-title" x="410" y="170" text-anchor="middle" textLength="296" lengthAdjust="spacingAndGlyphs">Meadowglen Horning</text>

      <rect class="comb-spot" x="253" y="205" width="90" height="75" rx="6" role="img" aria-label="Wabenmuster"/>
      <ellipse class="bee-spot" cx="408" cy="240" rx="50" ry="34" role="img" aria-label="Zeichnung einer Honigbiene"/>
      <rect class="comb-spot" x="468" y="205" width="90" height="75" rx="6" role="img" aria-label="Wabenmuster"/>

      <line class="rule rule--short" x1="262" y1="288" x2="300" y2="288"/>
      <text class="sub-title" x="408" y="295" text-anchor="middle" textLength="190" lengthAdjust="spacingAndGlyphs">MEADOWGLEN-HONING</text>
      <line class="rule rule--short" x1="517" y1="288" x2="555" y2="288"/>

      <line class="rule" x1="251" y1="316" x2="565" y2="316"/>
      <text class="address" x="408" y="342" text-anchor="middle" textLength="268" lengthAdjust="spacingAndGlyphs">KONSTANTIN AND JUTTA BRÜGGL</text>
      <text class="address" x="408" y="363" text-anchor="middle" textLength="300" lengthAdjust="spacingAndGlyphs">BIRKENWINKL 7, 84172 LINDACH AM FORST</text>
    </svg>
  </section>

</main>
</body>
</html>
```